Cedar Hall letterhead

We changed our name and logo now need letterhead.
3-4/72 Harlow Street Elmsford 2163
www.cedarhall.org.au
info@cedarhall.org.au
ph: 02 97584120

At this stage, we are preferencing Design #: 5398880 and Design #5401338

```html
<!DOCTYPE html>
<html lang="en">
<head>
<meta charset="utf-8">
<title>Cedar Hall Letterhead</title>
<link href="https://fonts.googleapis.com/css2?family=Open+Sans:wght@400;600&display=swap" rel="stylesheet">
<style>
  :root {
    --backdrop: #ececec;
    --paper: #ffffff;
    --ink: #2b2b2b;
    --brand: #7d91a5;
    --brand-deep: #5f7488;
    --brand-light: #a9bacb;
    --footer-ink: #8a9db0;
    --signature-ink: #2f4f9c;
  }
  * { box-sizing: border-box; margin: 0; padding: 0; }
  html, body {
    width: 1200px; height: 1000px; overflow: hidden;
    background: var(--backdrop);
    font-family: "Open Sans", Arial, sans-serif;
  }
  .letterhead {
    position: absolute; left: 270px; top: 33px;
    width: 660px; height: 934px;
    background: var(--paper);
    box-shadow: 0 2px 10px rgba(0,0,0,0.12);
    color: var(--ink);
  }
  .brand {
    position: absolute; left: 48px; top: 44px;
    display: flex; align-items: center; gap: 12px;
  }
  .brand-mark {
    width: 92px; height: 92px; border-radius: 50%;
    background: var(--brand);
  }
  .brand-name {
    font-size: 20px; font-weight: 400; color: var(--brand-deep);
    letter-spacing: 0.5px;
  }
  .recipient {
    position: absolute; left: 48px; top: 300px;
    font-size: 10.5px; line-height: 14px; font-style: normal;
  }
  .letter-body {
    position: absolute; left: 48px; top: 385px; width: 520px;
    font-size: 10.5px; line-height: 14.5px;
  }
  .letter-body p { margin-bottom: 14px; }
  .signature {
    position: absolute; left: 48px; top: 660px;
    width: 130px; height: 64px;
    background: linear-gradient(135deg, rgba(47,79,156,0.18), rgba(47,79,156,0.06));
    border-radius: 4px;
  }
  .signatory {
    position: absolute; left: 48px; top: 734px;
    font-size: 10.5px; line-height: 14px;
  }
  .contact {
    position: absolute; right: 48px; bottom: 48px;
    text-align: right; color: var(--footer-ink);
    font-size: 11px; line-height: 16px;
  }
  .contact-label { font-weight: 600; color: var(--brand-deep); }
  .footer-band {
    position: absolute; left: 0; right: 0; bottom: 0; height: 14px;
    background: linear-gradient(90deg, var(--brand-light), var(--brand), var(--brand-light));
  }
</style>
</head>
<body>
  <main class="letterhead">
    <header class="brand">
      <div class="brand-mark"></div>
      <span class="brand-name">Cedar Hall</span>
    </header>

    <address class="recipient">
      Mr. Daniel Brooks<br>
      Commercial Director<br>
      2417 County Road 90<br>
      Ellison, Mo 64810
    </address>

    <section class="letter-body">
      <p>Designing an effective letterhead is a unique challenge. Sometimes your letterhead design will be the first interaction a customer has had with a particular company, while other times it will be used to reinforce the brand identity. It's crucial to get the details right, but to also produce something that's tactile, eye-catching, and memorable. Designing an effective letterhead is a unique challenge. Sometimes your letterhead design will be the first interaction a customer has had with a particular company, while other times it will be used to reinforce the brand identity. It's crucial to get the details right, but to also produce something that's tactile, eye-catching, and memorable. Designing an effective letterhead is a unique challenge.</p>
      <p>Sometimes your letterhead design will be the first interaction a customer has had with a particular company, while other times it will be used to reinforce the brand identity. It's crucial to get the details right, but to also produce something that's tactile, eye-catching, and memorable. Designing an effective letterhead is a unique challenge. Sometimes your letterhead design will be the first interaction a customer has had with a particular company, while other times it will be used to reinforce the brand identity. It's crucial to get the details right, but to also produce something that's tactile, eye-catching, and memorable.</p>
    </section>

    <div class="signature" role="img" aria-label="Handwritten signature of Daniel Brooks"></div>
    <div class="signatory">Daniel Brooks<br>Commercial Director</div>

    <footer class="contact">
      3-4/72 Harlow Street Elmsford 2163<br>
      <span class="contact-label">Phone:</span> 02 97584120 &nbsp;&nbsp; <span class="contact-label">Email:</span> info@cedarhall.org.au<br>
      www.cedarhall.org.au
    </footer>
    <div class="footer-band"></div>
  </main>
</body>
</html>
```